R Hendrow tile

This add will be posted on a shopping cart at grocery store. I have limited space and need something to tie in all my info.Add will be top to bottom not horizontal
R. Hendrow
Custom Tile & Marble
"4 generations of Service"
Our slogan is: creating the most beautiful living spaces
614-283-7150
www.hendrowtile-example.com
email:rkbloom42@mailpost-example.com
in business since 1975
We would like to use the color yellow in the design and R. Hendrow has to be script font to match our trucks.

tile & marble flooring,walls, complete bathroom renovations new homes,remodels,

Shopping

ffc214
000000
b1b1b1
f37123

• Would like yellow to be used sparingly all other colors are just a suggestion. Need R. Hendrow To be in Script all other wording to be straight
• all contact info,other colors to tie into yellow

```html
<!DOCTYPE html>
<html lang="en">
<head>
<meta charset="utf-8">
<title>R. Hendrow Custom Tile &amp; Marble</title>
<link rel="stylesheet" href="https://fonts.googleapis.com/css2?family=Arimo:wght@400;700&family=Lobster&display=swap">
<style>
  :root {
    --paper: #ffffff;
    --ink: #000000;
    --accent-yellow: #ffc214;
    --tile-grey: #b1b1b1;
    --rule-grey: #c4c4c4;
  }
  * { margin: 0; padding: 0; box-sizing: border-box; }
  html, body { width: 1200px; height: 848px; overflow: hidden; background: var(--paper); }
  .canvas { position: relative; width: 1200px; height: 848px; background: var(--paper); font-family: "Arimo", Arial, sans-serif; color: var(--ink); }
  .side-rule { position: absolute; top: 207px; width: 1.5px; height: 480px; background: var(--rule-grey); }
  .side-rule--left { left: 411px; }
  .side-rule--right { left: 760px; }
  .brand-name { position: absolute; left: 412px; width: 349px; top: 198px; text-align: center; font-family: "Lobster", cursive; font-size: 50px; line-height: 64px; letter-spacing: 1px; }
  .service-line { position: absolute; left: 478px; top: 282px; font-size: 18px; line-height: 20px; }
  .tagline { position: absolute; right: 473px; top: 303px; font-size: 14px; line-height: 16px; letter-spacing: 0.5px; }
  .tile-motif { position: absolute; left: 478px; top: 350px; width: 208px; height: 190px; background: linear-gradient(135deg, var(--accent-yellow) 0%, #f7d15e 45%, var(--tile-grey) 100%); opacity: 0.85; }
  .since { position: absolute; left: 412px; width: 364px; top: 549px; text-align: center; font-size: 14px; line-height: 16px; letter-spacing: 0.5px; }
  .phone { position: absolute; left: 412px; width: 368px; top: 602px; text-align: center; font-size: 22px; line-height: 26px; letter-spacing: 1.5px; color: var(--accent-yellow); }
  .contact { position: absolute; right: 510px; top: 631px; text-align: right; font-size: 14px; line-height: 15px; }
  .contact .value { color: var(--accent-yellow); }
  .slogan { position: absolute; left: 412px; width: 354px; top: 676px; text-align: center; font-size: 10.5px; line-height: 12px; letter-spacing: 0.8px; text-transform: uppercase; }
</style>
</head>
<body>
<main class="canvas">
  <div class="side-rule side-rule--left"></div>
  <div class="side-rule side-rule--right"></div>

  <h1 class="brand-name">R. Hendrow</h1>
  <p class="service-line">Custom Tile &amp; Marble</p>
  <p class="tagline">"4 generations of Service"</p>

  <div class="tile-motif" role="img" aria-label="Scattered isometric tile cubes in yellow and grey"></div>

  <p class="since">in business since 1975</p>
  <p class="phone">614-283-7150</p>
  <p class="contact">
    email:<span class="value">rkbloom42@mailpost-example.com</span><br>
    <span class="value">www.hendrowtile-example.com</span>
  </p>
  <p class="slogan">Creating the most beautiful living spaces</p>
</main>
</body>
</html>
```